Northgate Print and Paper Business

Hi, I need template designs for stationary as listed below using my Logo as per attached file;
1) Business Card (double sided)
2) Letterhead
3) With Compliments Slip
4) Return Address Label (Stickers)

```html
<!DOCTYPE html>
<html lang="en">
<head>
<meta charset="utf-8">
<title>Northgate Print and Paper Business – Business Card</title>
<link rel="stylesheet" href="https://fonts.googleapis.com/css2?family=Questrial&display=swap">
<style>
  :root {
    --backdrop: #e6e4e1;
    --card: #f1f1f1;
    --ink: #2a2a2a;
    --magenta: #c8127a;
    --green: #2f9a3a;
    --lime: #7bb62c;
    --plum: #9c1f6e;
  }
  html, body {
    margin: 0;
    width: 1200px;
    height: 900px;
    overflow: hidden;
    background: var(--backdrop);
    font-family: "Questrial", "Century Gothic", sans-serif;
    color: var(--ink);
  }
  .stationery {
    position: relative;
    width: 1200px;
    height: 900px;
  }
  .card {
    position: absolute;
    top: 275px;
    width: 540px;
    height: 350px;
    background: var(--card);
    box-shadow: 0 2px 10px rgba(0,0,0,0.12);
    overflow: hidden;
  }
  .card--contact { left: 40px; }
  .card--brand { left: 620px; }

  /* Contact side */
  .holder {
    position: absolute;
    left: 100px;
    top: 38px;
    width: 280px;
    padding-bottom: 10px;
    border-bottom: 1.5px solid var(--magenta);
  }
  .holder__name {
    font-size: 27px;
    letter-spacing: 0.2px;
  }
  .holder__role {
    font-size: 11px;
    letter-spacing: 0.8px;
    margin-left: 6px;
  }
  .contact-list {
    position: absolute;
    left: 40px;
    top: 96px;
    margin: 0;
    padding: 0;
    list-style: none;
    font-size: 14px;
    line-height: 18px;
  }
  .contact-list__label {
    display: inline-block;
    width: 22px;
    color: var(--magenta);
    font-size: 12px;
  }
  .address {
    position: absolute;
    left: 40px;
    top: 160px;
    margin: 0;
    font-style: normal;
    font-size: 14px;
    line-height: 18px;
  }
  .website {
    position: absolute;
    left: 40px;
    top: 212px;
    font-size: 14px;
  }
  .brand-band {
    position: absolute;
    left: 0;
    bottom: 0;
  }

  /* Brand side */
  .brand-name {
    position: absolute;
    left: 0;
    right: 0;
    top: 128px;
    text-align: center;
    font-size: 34px;
    line-height: 42px;
    color: var(--ink);
  }
</style>
</head>
<body>
<main class="stationery">

  <section class="card card--contact">
    <div class="holder">
      <span class="holder__name">Lena Hartwell</span><span class="holder__role">MANAGER</span>
    </div>
    <ul class="contact-list">
      <li><span class="contact-list__label">T</span>+41 22 555 0142</li>
      <li><span class="contact-list__label">M</span>+41 78 555 0199</li>
      <li><span class="contact-list__label">E</span>lena@northgate-print.com</li>
    </ul>
    <address class="address">Haus Linde, Mühlegasse 7<br>CH-4051 Basel</address>
    <div class="website">www.northgate-print.com</div>
    <svg class="brand-band" width="540" height="350" viewBox="0 0 540 350" role="img" aria-label="Brand ribbon decoration area in green and magenta">
      <defs>
        <linearGradient id="band-tone" x1="0" y1="1" x2="1" y2="0">
          <stop offset="0" stop-color="var(--plum)" stop-opacity="0.55"/>
          <stop offset="0.5" stop-color="var(--lime)" stop-opacity="0.45"/>
          <stop offset="1" stop-color="var(--green)" stop-opacity="0.55"/>
        </linearGradient>
      </defs>
      <rect x="230" y="240" width="310" height="110" fill="url(#band-tone)"/>
    </svg>
  </section>

  <section class="card card--brand">
    <div class="brand-name">Northgate Print<br>and Paper Business</div>
  </section>

</main>
</body>
</html>
```